I am looking for a designer for my Gratitude Journal cover design. This is a daily gratitude journal designed for women. The interior features colored pages with a daily gratitude section, weekly habit tracker, and monthly reflection. The journal has enough space for a 12-week journaling.
Book size: 6x 9 inches
Paperback Print Book
Page count: 117
Platform: Nimbo BPX
Book title: I’m Unfinished, Who Cares?
Design Style:
-Boho style color and graphics, color choice is free but must follow color psychology, no pure black. The color and styling should correlate to the interior pages (In the attachment).
-There could be a female silhouette on the front cover, but not as big as the whole cover. (doesn’t have to if not looking good)
-No text or interior page preview on the back cover. Only pen name logo on the bottom middle of the back cover and make it small and subtle. (Pen name logo attached)
-Book title on front cover and spine, author name only on spine (Author name: Tobias Wexley).
-No other text on the front cover.
All design elements including fonts must be commercially licensed, and you must provide source files and commercial licenses of them together as part of the delivery.
nimbo.example

```html
<!DOCTYPE html>
<html lang="en">
<head>
<meta charset="utf-8">
<title>I’m Unfinished, Who Cares? — Cover Wrap</title>
<link rel="stylesheet" href="https://fonts.googleapis.com/css2?family=Fraunces:opsz,wght@9..144,600;9..144,700&display=swap">
<style>
  :root {
    --page: #ffffff;
    --cover: #f7f7f7;
    --spine-line: #cfcfcf;
    --ink-teal: #6c9690;
    --leaf-teal: #a9d9d5;
    --leaf-peach: #fadcc0;
    --leaf-sand: #e3b98b;
    --mark-dot: #24324a;
  }
  html, body {
    margin: 0;
    padding: 0;
    width: 1199px;
    height: 1200px;
    overflow: hidden;
    background: var(--page);
  }
  .canvas {
    position: relative;
    width: 1199px;
    height: 1200px;
    background: var(--page);
    font-family: "Fraunces", Georgia, serif;
  }
  .wrap {
    position: absolute;
    left: 39px;
    top: 174px;
    width: 1112px;
    height: 804px;
    background: var(--cover);
  }
  .back-cover {
    position: absolute;
    left: 0;
    top: 0;
    width: 528px;
    height: 804px;
  }
  .pen-name-mark {
    position: absolute;
    left: 50%;
    top: 668px;
    transform: translateX(-50%);
    display: flex;
    align-items: center;
    gap: 8px;
    white-space: nowrap;
  }
  .pen-name-mark__dot {
    width: 14px;
    height: 14px;
    border-radius: 50%;
    background: var(--mark-dot);
  }
  .pen-name-mark__name {
    font-size: 15px;
    font-weight: 600;
    color: var(--mark-dot);
    letter-spacing: 0.02em;
  }
  .spine {
    position: absolute;
    left: 528px;
    top: 0;
    width: 57px;
    height: 804px;
    box-sizing: border-box;
    border: 1px solid var(--spine-line);
  }
  .spine__author {
    position: absolute;
    left: 50%;
    top: 306px;
    margin: 0;
    transform: translateX(-50%);
    writing-mode: vertical-rl;
    white-space: nowrap;
    font-size: 25px;
    font-weight: 700;
    line-height: 1;
    color: var(--ink-teal);
  }
  .front-cover {
    position: absolute;
    left: 585px;
    top: 0;
    width: 527px;
    height: 804px;
  }
  .front-cover__title {
    position: absolute;
    left: 38px;
    top: 40px;
    margin: 0;
    font-size: 67px;
    font-weight: 700;
    line-height: 61px;
    letter-spacing: -0.01em;
    color: var(--ink-teal);
  }
  .front-cover__title span { display: block; }
  .front-cover__leaves {
    position: absolute;
    left: 0;
    top: 285px;
    width: 527px;
    height: 332px;
    background:
      radial-gradient(ellipse at 18% 30%, var(--leaf-teal) 0%, transparent 45%),
      radial-gradient(ellipse at 45% 20%, var(--leaf-peach) 0%, transparent 40%),
      radial-gradient(ellipse at 85% 25%, var(--leaf-sand) 0%, transparent 42%),
      radial-gradient(ellipse at 55% 55%, var(--leaf-teal) 0%, transparent 40%),
      radial-gradient(ellipse at 18% 78%, var(--leaf-sand) 0%, transparent 42%),
      radial-gradient(ellipse at 60% 85%, var(--leaf-peach) 0%, transparent 40%),
      radial-gradient(ellipse at 88% 75%, var(--leaf-teal) 0%, transparent 40%),
      #ffffff;
  }
</style>
</head>
<body>
  <main class="canvas">
    <section class="wrap">
      <div class="back-cover">
        <div class="pen-name-mark">
          <span class="pen-name-mark__dot"></span>
          <span class="pen-name-mark__name">Tobias Wexley</span>
        </div>
      </div>
      <div class="spine">
        <p class="spine__author">Tobias Wexley</p>
      </div>
      <div class="front-cover">
        <h1 class="front-cover__title">
          <span>I’m</span>
          <span>Unfinished,</span>
          <span>Who Cares?</span>
        </h1>
        <div class="front-cover__leaves" role="img" aria-label="Scattered boho palm leaves in soft teal, peach and sand tones"></div>
      </div>
    </section>
  </main>
</body>
</html>
```